Card design for Heating and Cooling company

this is for a heating and cooling company we recently updated our logo and need to update our cards. We attached our logo so you can incorporate it into the card. We specialize in residential and commercial furnace and air condition repairs. Have been in business since 2014.

Phone number 555.284.9137

We need the following phrases
:Repairs, Installations, and maintenance
:Quality work at reasonable prices
:residential/commercial
:Licensed &Insured
:Email Pinegrovehvac47@mailbox-example.com
Name: Teodor K (Ted)
Also on back side I would like my logo with wording :Thank you for your business and refferal

Industry/Entity Type

Hvac

Contact Information for Business Card

:residential/commercial
:Licensed & Insured
Name: Teodor K (Ted)
Number:555.284.9136

Requirements
Must have
• Blue and red colors
Nice to have
• Maybe a pic of a furnace or air conditioner

```html
<!DOCTYPE html>
<html lang="en">
<head>
<meta charset="utf-8">
<title>Pinegrove Heating &amp; Cooling — Business Card</title>
<link rel="stylesheet" href="https://fonts.googleapis.com/css2?family=Arimo:wght@400;700&display=swap">
<style>
  :root {
    --page-bg: #4a4a4a;
    --card-blue: #0000ff;
    --panel-sky: #00a8f0;
    --accent-red: #ff1a1a;
    --ink-black: #000000;
    --ink-blue: #0000e6;
    --brand-orange: #ff7a00;
  }
  * { box-sizing: border-box; margin: 0; padding: 0; }
  html, body {
    width: 1200px; height: 1200px; overflow: hidden;
    background: var(--page-bg);
    font-family: "Arimo", Arial, sans-serif;
  }
  .sheet {
    width: 1200px; height: 1200px;
    display: flex; flex-direction: column; align-items: center; justify-content: center;
    gap: 40px;
  }
  .card {
    position: relative;
    width: 960px; height: 500px;
    background: var(--card-blue);
    overflow: hidden;
  }
  .card-panel { position: absolute; inset: 0; }

  .brand {
    position: absolute;
    display: flex; align-items: center; gap: 14px;
    color: var(--ink-black);
    font-weight: 700;
  }
  .brand-dot {
    width: 46px; height: 46px; border-radius: 50%;
    background: var(--panel-sky);
    flex: none;
  }
  .brand-name { line-height: 1.05; }
  .brand-name .line-main { display: block; font-size: 52px; letter-spacing: 1px; }
  .brand-name .line-sub { display: block; font-size: 20px; letter-spacing: 6px; }

  .card-front .brand { left: 60px; top: 150px; }
  .owner {
    position: absolute; left: 70px; top: 330px;
    color: var(--ink-black);
  }
  .owner-name { font-size: 54px; font-weight: 400; letter-spacing: 1px; line-height: 1; }
  .owner-title { font-size: 26px; margin-top: 4px; }

  .contact {
    position: absolute; left: 585px; top: 190px; width: 360px;
    color: var(--ink-blue);
  }
  .contact-row { display: flex; align-items: center; gap: 10px; }
  .contact-row svg { flex: none; }
  .contact-email { font-size: 17px; }
  .contact-phone { font-size: 30px; margin-top: 14px; }
  .services { list-style: none; margin-top: 22px; font-size: 20px; line-height: 1.9; }

  .card-back .brand { left: 50%; top: 160px; transform: translateX(-50%); }
  .thanks {
    position: absolute; left: 110px; bottom: 70px;
    color: var(--accent-red);
    font-size: 40px;
  }
</style>
</head>
<body>
<main class="sheet">

  <section class="card card-front" aria-label="Card front">
    <svg class="card-panel" width="960" height="500" viewBox="0 0 960 500" aria-hidden="true">
      <path d="M560 0 H960 V440 C880 430 800 470 700 470 C640 470 600 455 560 440 Z" fill="var(--panel-sky)"/>
      <path d="M560 135 C680 110 800 85 960 150" fill="none" stroke="var(--accent-red)" stroke-width="5"/>
      <path d="M540 430 C610 465 690 480 760 468 C840 455 900 440 960 442" fill="none" stroke="var(--accent-red)" stroke-width="5"/>
    </svg>

    <div class="brand">
      <span class="brand-dot"></span>
      <span class="brand-name"><span class="line-main">PINEGROVE</span><span class="line-sub">HEATING &amp; COOLING</span></span>
    </div>

    <div class="owner">
      <p class="owner-name">TEODOR K</p>
      <p class="owner-title">Owner</p>
    </div>

    <div class="contact">
      <p class="contact-row contact-email">
        <svg width="28" height="20" viewBox="0 0 28 20"><rect x="1.5" y="1.5" width="25" height="17" fill="none" stroke="var(--accent-red)" stroke-width="2"/><path d="M1.5 1.5 L14 11 L26.5 1.5 M1.5 18.5 L11 9 M26.5 18.5 L17 9" fill="none" stroke="var(--accent-red)" stroke-width="2"/></svg>
        Pinegrovehvac47@mailbox-example.com
      </p>
      <p class="contact-row contact-phone">
        <svg width="30" height="30" viewBox="0 0 30 30"><circle cx="15" cy="15" r="15" fill="var(--accent-red)"/><path d="M10 7 L13 7 L14 11 L12 13 C13 16 14 17 17 18 L19 16 L23 17 L23 20 C23 22 21 23 19 23 C13 22 8 17 7 11 C7 9 8 7 10 7 Z" fill="var(--card-blue)"/></svg>
        555.284.9137
      </p>
      <ul class="services">
        <li>Repairs, Installations, and maintenance</li>
        <li>Quality work at reasonable prices</li>
        <li>residential/commercial</li>
        <li>Licensed &amp;Insured</li>
      </ul>
    </div>
  </section>

  <section class="card card-back" aria-label="Card back">
    <div class="brand">
      <span class="brand-dot"></span>
      <span class="brand-name"><span class="line-main">PINEGROVE</span><span class="line-sub">HEATING &amp; COOLING</span></span>
    </div>
    <p class="thanks">Thank you for your business and refferal</p>
  </section>

</main>
</body>
</html>
```